Lark IT Support company needs a flyer

This flyer will be delivered by hand to prospective customers in a door drop campaign.
Double sided A6
We support SMEs in Central London mainly Lark networks. We also supply managed services including email and internet connectivity.
The target audience is office managers, receptionists and business owners.
It will be extremely simple and illustration mainly.
Any ideas are welcome but we quite like the following:
A text poster saying
"Make IT easy" or something like that.
An illustration of two people, the client and us. Us juggling web, IT etc and the Client able to concentrate on their job.
Copy is being written by a professional copywriter, content of which will depend on the flyer design.
Target Market(s)
Small SMEs using Pomelo Lark computers, design companies, agencies etc.
Industry/Entity Type
Technical Service
Requirements
Must have
- Our number - 0203 555 0184
- Our email - info@quill-node.it
- Our web address - www.quill-node.it
Nice to have
- Some clever eye catching designs
Should not have
- Too much text
- Overly complicated design

```html
<!DOCTYPE html>
<html lang="en">
<head>
<meta charset="utf-8">
<title>Quill Node – IT Support Flyer</title>
<link href="https://fonts.googleapis.com/css2?family=Anton&family=Lato:wght@400;700&family=Oswald:wght@500;600&display=swap" rel="stylesheet">
<style>
:root{
  --green:#9bc53d;
  --green-dark:#7aa52a;
  --orange:#ef6c1a;
  --orange-deep:#e35b0e;
  --ink:#1e1e1e;
  --text:#333333;
  --white:#ffffff;
  --stage:#e9e6e1;
  --photo-a:#2a3c55;
  --photo-b:#8fa6bf;
}
*{margin:0;padding:0;box-sizing:border-box}
html,body{width:1200px;height:907px;overflow:hidden;background:var(--stage)}
.canvas{position:relative;width:1200px;height:907px}
.flyer{position:absolute;top:90px;width:523px;height:736px;background:var(--white);overflow:hidden;box-shadow:0 2px 8px rgba(0,0,0,.25);font-family:"Lato",sans-serif;color:var(--text)}
.flyer--front{left:70px}
.flyer--back{left:628px}
.flyer__art{position:absolute;inset:0}
.abs{position:absolute}

/* front */
.brand-badge{left:347px;top:230px;width:160px;height:160px;border-radius:50%;background:var(--ink);border:5px solid var(--white);box-shadow:0 0 0 2px #ccc;display:flex;align-items:center;justify-content:center}
.brand-name{font-family:"Lato",sans-serif;font-weight:700;color:var(--green);font-size:22px;white-space:nowrap}
.headline{left:0;width:523px;top:395px;text-align:center;font-family:"Anton",sans-serif;font-size:82px;line-height:1;letter-spacing:1px;color:var(--ink)}
.headline .accent{color:var(--orange-deep)}
.kicker{left:0;width:523px;top:546px;text-align:center;font-size:20px;color:var(--orange);letter-spacing:.5px}
.tagline{left:0;width:523px;top:580px;text-align:center;font-size:33px;color:var(--ink)}
.subline{left:0;width:523px;top:632px;text-align:center;font-size:17.5px;line-height:23px;color:var(--ink)}
.rule{left:0;width:523px;top:692px;height:3px;background:var(--orange)}
.contact-bar{left:0;top:698px;width:523px;height:38px;background:var(--ink);display:flex;align-items:center;justify-content:space-between;padding:0 12px;font-size:12.5px;color:var(--white)}
.contact-bar span{display:flex;align-items:center;gap:6px}
.contact-bar svg{flex:none}

/* back */
.team-photo{left:18px;top:138px;width:172px;height:172px;border-radius:50%;border:5px solid var(--white);box-shadow:0 0 0 1px #bbb;background:linear-gradient(160deg,#dfe4ea,#6f86a3)}
.section-pill{left:0;top:328px;height:28px;padding:0 14px 0 20px;background:var(--green);border-radius:0 14px 14px 0;font-family:"Oswald",sans-serif;font-weight:600;font-size:18px;line-height:28px;color:var(--ink)}
.services{left:22px;top:370px;list-style:none}
.services li{height:29.8px;display:flex;align-items:center;font-size:14px;color:var(--text)}
.services li::before{content:"";width:10px;height:10px;border-radius:50%;background:var(--orange);margin-right:22px}
.back-brand{left:26px;top:652px}
.about-panel{left:265px;top:360px;width:258px;height:332px;background:linear-gradient(90deg,var(--orange),#f39a4c)}
.about-pill{right:0;top:391px;height:26px;padding:0 14px;background:var(--ink);border-radius:13px 0 0 13px;font-family:"Oswald",sans-serif;font-weight:500;font-size:18px;line-height:26px;color:var(--white)}
.about-text{left:282px;top:428px;width:225px;font-size:11.6px;line-height:15px;color:var(--white);text-align:justify;text-align-last:right}
.map{left:279px;top:587px;width:225px;height:88px;border-radius:16px;border:3px solid var(--ink);background:linear-gradient(135deg,#ecebe6,#d8d6cf)}
.web-rule{left:0;top:693px;width:265px;height:3px;background:var(--green)}
.web-bar{left:0;top:697px;width:523px;height:39px;background:var(--ink);color:var(--white);text-align:center;font-size:15px;line-height:39px;letter-spacing:3px}
</style>
</head>
<body>
<div class="canvas">

  <!-- Front side -->
  <section class="flyer flyer--front">
    <svg class="flyer__art" width="523" height="736" viewBox="0 0 523 736">
      <defs>
        <linearGradient id="frontPhoto" x1="0" y1="0" x2="1" y2="1">
          <stop offset="0" stop-color="#3a4a62"/>
          <stop offset=".55" stop-color="#7f9ab6"/>
          <stop offset="1" stop-color="#c9d6e2"/>
        </linearGradient>
        <linearGradient id="frontGreen" x1="0" y1="0" x2="1" y2="0">
          <stop offset="0" stop-color="#8cbf2e"/>
          <stop offset=".5" stop-color="#a8cf4a"/>
          <stop offset="1" stop-color="#8cbf2e"/>
        </linearGradient>
      </defs>
      <rect width="523" height="370" fill="url(#frontPhoto)" role="img" aria-label="Photo of a businessman holding connected laptop, tablet, phone and globe network"/>
      <path d="M0,337 C250,332 455,225 495,0 L523,0 L523,736 L0,736Z" fill="var(--orange)"/>
      <path d="M0,346 C255,342 468,232 508,0 L523,0 L523,736 L0,736Z" fill="var(--white)"/>
      <path d="M0,352 C258,348 474,238 515,0 L523,0 L523,736 L0,736Z" fill="var(--ink)"/>
      <path d="M0,360 C262,356 480,246 523,10 L523,736 L0,736Z" fill="url(#frontGreen)"/>
      <path d="M0,545 Q262,485 523,545 L523,736 L0,736Z" fill="var(--orange)"/>
      <path d="M0,553 Q262,495 523,553 L523,736 L0,736Z" fill="var(--ink)"/>
      <path d="M0,562 Q262,506 523,562 L523,736 L0,736Z" fill="var(--white)"/>
    </svg>
    <div class="abs brand-badge"><span class="brand-name">Quill Node</span></div>
    <h1 class="abs headline"><span class="accent">Make</span> IT easy</h1>
    <p class="abs kicker">WE'RE ABOUT</p>
    <h2 class="abs tagline">Friendly &amp; Reliable Tech Support</h2>
    <p class="abs subline">IT Support, Consultancy and Project Management<br>A one stop shop for all of your business' IT needs</p>
    <div class="abs rule"></div>
    <div class="abs contact-bar">
      <span><svg width="11" height="11" viewBox="0 0 24 24"><path fill="var(--green)" d="M6.6 10.8a15 15 0 006.6 6.6l2.2-2.2c.3-.3.7-.4 1-.2 1.1.4 2.3.6 3.6.6.6 0 1 .4 1 1V20c0 .6-.4 1-1 1A17 17 0 013 4c0-.6.4-1 1-1h3.5c.6 0 1 .4 1 1 0 1.3.2 2.5.6 3.6.1.3 0 .7-.2 1z"/></svg>0203 555 0184</span>
      <span><svg width="10" height="13" viewBox="0 0 20 26"><path fill="var(--green)" d="M10 0a10 10 0 00-10 10c0 7.5 10 16 10 16s10-8.5 10-16A10 10 0 0010 0zm0 14a4 4 0 110-8 4 4 0 010 8z"/></svg>12 - 16 Harrow Lane, London, SE1 9ZZ</span>
      <span><svg width="14" height="10" viewBox="0 0 28 20"><rect width="28" height="20" rx="2" fill="var(--green)"/><path d="M1 1l13 10L27 1" stroke="var(--ink)" stroke-width="2" fill="none"/></svg>info@quill-node.it</span>
    </div>
  </section>

  <!-- Back side -->
  <section class="flyer flyer--back">
    <svg class="flyer__art" width="523" height="736" viewBox="0 0 523 736">
      <defs>
        <linearGradient id="backPhoto" x1="0" y1="0" x2="1" y2="0">
          <stop offset="0" stop-color="#2f8fbf"/>
          <stop offset=".5" stop-color="#a9d3e3"/>
          <stop offset="1" stop-color="#1d2a4a"/>
        </linearGradient>
      </defs>
      <rect width="523" height="370" fill="url(#backPhoto)" role="img" aria-label="Photo of a businessman drawing a cloud network diagram with chalk"/>
      <path d="M0,0 L70,0 C40,60 20,120 0,170Z" fill="var(--white)"/>
      <path d="M0,170 C20,120 40,60 70,0 L80,0 C48,70 25,140 0,200Z" fill="var(--ink)"/>
      <path d="M0,235 C150,330 330,370 523,322 L523,736 L0,736Z" fill="var(--orange)"/>
      <path d="M0,245 C150,338 330,378 523,332 L523,736 L0,736Z" fill="var(--green)"/>
      <path d="M0,255 C150,346 330,384 523,342 L523,736 L0,736Z" fill="var(--ink)"/>
      <path d="M0,262 C150,353 330,390 523,350 L523,736 L0,736Z" fill="var(--white)"/>
    </svg>
    <div class="abs team-photo" role="img" aria-label="Photo of a smiling office team"></div>
    <div class="abs about-panel"></div>
    <h2 class="abs section-pill">Our Services</h2>
    <ul class="abs services">
      <li>IT Support</li>
      <li>IT Consultancy</li>
      <li>IT Project Management</li>
      <li>Cloud based backup</li>
      <li>Internet connectivity</li>
      <li>Cloud based Email</li>
      <li>Relocation</li>
      <li>Monitoring</li>
      <li>Span Prevation</li>
    </ul>
    <div class="abs back-brand"><span class="brand-name">Quill Node</span></div>
    <h2 class="abs about-pill">About Us</h2>
    <p class="abs about-text">Quill Node was formed in 2004 as an IT support company servicing London's advertising and media companies. In the last 11 years we've grown to support all three major platforms: Pomelo, Mosaic and Lumen. We now support a far wider demographic including Finance, Retail, Governing bodies and Property to name just a few.</p>
    <div class="abs map" role="img" aria-label="Street map showing the office location"></div>
    <div class="abs web-rule"></div>
    <div class="abs web-bar">www.quill-node.it</div>
  </section>

</div>
</body>
</html>
```